" A Velmar iniciou suas atividades em Balneário Camboriú-SC há cerca de 30 dias. Atualmente funciona com um consultório de atendimento médico montado dentro de uma clínica maior, chamada Nefrovita. O objetivo ao longo do tempo é ocupar um espaço cada vez maior tornando uma clínica propriamente dita, com métodos diagnósticos agregados, porém, sempre no mesmo conceito de divisao de espaço com a Nefrovita. Assim, o primeiro passo é montar uma identidade própria, e tudo começa com a criaçao do logo e dos materiais de identidade, tal como receituários, papel timbrado, pastas, envelopes. "

```html
<!DOCTYPE html>
<html lang="pt-BR">
<head>
<meta charset="utf-8">
<title>Velmar-sc — Cartão de visita</title>
<link rel="stylesheet" href="https://fonts.googleapis.com/css2?family=Arimo:wght@400;700&family=Crimson+Text:wght@400&display=swap">
<style>
  :root {
    --backdrop: #3b3939;
    --card-white: #ffffff;
    --brand-red: #b3262b;
    --card-red-dark: #7e1519;
    --card-red-light: #a8282c;
    --ink-dark: #444244;
    --ink-light: #ffffff;
  }
  * { margin: 0; padding: 0; box-sizing: border-box; }
  html, body {
    width: 1200px;
    height: 1200px;
    overflow: hidden;
    background: var(--backdrop);
  }
  .canvas {
    position: relative;
    width: 1200px;
    height: 1200px;
  }
  .card {
    position: absolute;
    left: 161px;
    width: 878px;
    height: 480px;
  }
  .card--front {
    top: 108px;
    background: var(--card-white);
  }
  .card--back {
    top: 624px;
    background: radial-gradient(ellipse at 40% 40%, var(--card-red-light) 0%, var(--card-red-dark) 100%);
    color: var(--ink-light);
  }
  .brand {
    position: absolute;
    left: 322px;
    top: 200px;
    display: flex;
    align-items: center;
    gap: 16px;
  }
  .brand__dot {
    width: 26px;
    height: 26px;
    border-radius: 50%;
    background: var(--brand-red);
  }
  .brand__name {
    font-family: "Arimo", Arial, sans-serif;
    font-weight: 700;
    font-size: 54px;
    line-height: 1;
    color: var(--ink-dark);
    letter-spacing: -1px;
  }
  .brand__tagline {
    position: absolute;
    left: 530px;
    top: 262px;
    font-family: "Arimo", Arial, sans-serif;
    font-size: 13px;
    color: var(--brand-red);
  }
  .doctor {
    position: absolute;
    left: 518px;
    top: 150px;
    font-family: "Crimson Text", Georgia, serif;
  }
  .doctor__name {
    font-size: 40px;
    font-weight: 400;
    line-height: 1;
    letter-spacing: 0.5px;
  }
  .doctor__register {
    display: block;
    margin: 4px 0 0 148px;
    font-size: 13px;
  }
  .doctor__specialty {
    margin-left: 80px;
    font-size: 20px;
    line-height: 26px;
  }
  .contact {
    position: absolute;
    left: 506px;
    top: 428px;
    font-family: "Arimo", Arial, sans-serif;
    font-weight: 700;
    font-size: 15px;
    line-height: 18px;
    list-style: none;
  }
</style>
</head>
<body>
<main class="canvas">
  <section class="card card--front" aria-label="Frente do cartão">
    <div class="brand">
      <span class="brand__dot"></span>
      <span class="brand__name">Velmar-sc</span>
    </div>
    <p class="brand__tagline">Saúde Cardiovascular</p>
  </section>

  <section class="card card--back" aria-label="Verso do cartão">
    <div class="doctor">
      <h1 class="doctor__name">Dr.Rafael Denardi</h1>
      <span class="doctor__register">CRM-SC 40218</span>
      <p class="doctor__specialty">Cardiologista</p>
      <p class="doctor__specialty">Ecocardiografista</p>
    </div>
    <ul class="contact">
      <li>Endereço: Rua das Palmeiras ,482</li>
      <li>Balneário Camboriú-SC (anexo a Nefrovita-sc)</li>
      <li>Telefone: (47)35550142 / 35550187</li>
    </ul>
  </section>
</main>
</body>
</html>
```